Brightwell Mechanical - Business Card Design

We would like a dark (likely black) themed business card to be able to hand out to potential clients. We may list our services on the card or keep it clean. Unsure. Logo attached

```html
<!DOCTYPE html>
<html lang="en">
<head>
<meta charset="utf-8">
<title>Brightwell Mechanical – Business Card</title>
<link href="https://fonts.googleapis.com/css2?family=Poppins:wght@400;500;700;800&display=swap" rel="stylesheet">
<style>
  :root {
    --page: #131417;
    --card: #1e2125;
    --card-edge: #272b30;
    --blue: #1f78c8;
    --orange: #f0652a;
    --text: #e9ecef;
  }
  * { box-sizing: border-box; margin: 0; padding: 0; }
  html, body { width: 1200px; height: 800px; overflow: hidden; }
  body {
    background: var(--page);
    font-family: "Poppins", Arial, sans-serif;
    display: flex;
    align-items: center;
    justify-content: center;
    gap: 40px;
  }
  .card {
    position: relative;
    width: 520px;
    height: 300px;
    background: var(--card);
    border: 1px solid var(--card-edge);
    border-radius: 18px;
    overflow: hidden;
  }
  /* Front */
  .card-front { display: flex; align-items: center; justify-content: center; }
  .brand { display: flex; align-items: center; gap: 14px; }
  .brand-dot {
    width: 46px; height: 46px; border-radius: 50%;
    background: var(--orange);
    flex: none;
  }
  .brand-name {
    color: var(--blue);
    font-weight: 800;
    text-transform: uppercase;
    line-height: 1.05;
    letter-spacing: 0.5px;
  }
  .card-front .brand-name { font-size: 30px; }
  /* Back */
  .card-back .brand { position: absolute; top: 34px; right: 34px; gap: 10px; }
  .card-back .brand-dot { width: 30px; height: 30px; }
  .card-back .brand-name { font-size: 19px; text-align: left; }
  .divider {
    position: absolute; left: 34px; right: 34px; top: 190px;
    height: 1px; background: var(--blue);
  }
  .person { position: absolute; left: 34px; top: 110px; }
  .person-name { color: var(--blue); font-weight: 700; font-size: 20px; text-transform: uppercase; line-height: 1.1; }
  .person-role { color: var(--orange); font-weight: 500; font-size: 13px; text-transform: uppercase; letter-spacing: 0.5px; }
  .address {
    position: absolute; right: 34px; top: 112px;
    text-align: right; color: var(--text);
    font-size: 12px; line-height: 1.5;
  }
  .address .web-accent { color: var(--orange); }
  .contacts { position: absolute; left: 34px; top: 206px; list-style: none; }
  .contacts li {
    display: flex; align-items: center; gap: 10px;
    color: var(--text); font-size: 12.5px; line-height: 1; margin-bottom: 9px;
  }
  .icon {
    width: 18px; height: 18px; border-radius: 50%;
    background: var(--orange);
    display: flex; align-items: center; justify-content: center; flex: none;
  }
  .icon svg { width: 10px; height: 10px; fill: var(--card); }
</style>
</head>
<body>

<section class="card card-front" aria-label="Card front">
  <div class="brand">
    <span class="brand-dot"></span>
    <span class="brand-name">Brightwell<br>Mechanical Inc</span>
  </div>
</section>

<section class="card card-back" aria-label="Card back">
  <div class="brand">
    <span class="brand-dot"></span>
    <span class="brand-name">Brightwell<br>Mechanical Inc</span>
  </div>

  <div class="person">
    <p class="person-name">Daniel Hart</p>
    <p class="person-role">Manager</p>
  </div>

  <address class="address" style="font-style:normal">
    PO Box 48, Harbour Road<br>
    2nd street Geelong<br>
    www.<span class="web-accent">brightwellmech</span>.com
  </address>

  <div class="divider"></div>

  <ul class="contacts">
    <li>
      <span class="icon"><svg viewBox="0 0 24 24"><path d="M6.6 10.8a15.1 15.1 0 0 0 6.6 6.6l2.2-2.2c.3-.3.7-.4 1-.2 1.1.4 2.3.6 3.6.6.6 0 1 .4 1 1V20c0 .6-.4 1-1 1A17 17 0 0 1 3 4c0-.6.4-1 1-1h3.5c.6 0 1 .4 1 1 0 1.3.2 2.5.6 3.6.1.3 0 .7-.2 1z"/></svg></span>
      +1 555 014 2290
    </li>
    <li>
      <span class="icon"><svg viewBox="0 0 24 24"><path d="M7 2h10a2 2 0 0 1 2 2v16a2 2 0 0 1-2 2H7a2 2 0 0 1-2-2V4a2 2 0 0 1 2-2zm0 3v13h10V5z"/></svg></span>
      +1 555 014 2291
    </li>
    <li>
      <span class="icon"><svg viewBox="0 0 24 24"><path d="M3 5h18v14H3zm2 2v.5l7 4.5 7-4.5V7zm0 2.8V17h14V9.8l-7 4.5z"/></svg></span>
      info@brightwellmech.com
    </li>
  </ul>
</section>

</body>
</html>
```